GUMMY OVAL MYLAR BAG

THIS PRODUCT IS INTENDED FOR CAREGIVER TO PATIENT TRANSFER ONLY AND SHALL NOT BE SOLD.
BACK :
(Marijuana Symbol top L)
INGREDIENTS: CORN SYRUP, WATER, SUGAR, GELATIN, ACTIVATED THC (FROM MICHIGAN GROWN CANNABIS), CITRIC ACID, VEGETABLE OIL, NATURAL AND ARTIFICIAL FLAVORS AND COLORS, CARNAUBA WAX
WARNING: CONTAINS THC.
KEEP OUT OF REACH OF CHILDREN
CORVANE TOXIN HELP BUREAU 1 800 555 0147
MADE BY A CAREGIVER LICENSED BY THE STATE OF MICHIGAN UNDER THE BRENWICK THERAPEUTIC HERB PROGRAM (BTHP) IN COMPLIANCE WITH THE 2008 BRENWICK THERAPEUTIC HERB ACT.
FOR USE BY INDIVIDUALS 21 YEARS OF AGE OR OLDER OR BY REGISTERED QUALIFYING PATIENTS ONLY.
(reversed out (white backing) with a black outline around the following:
WARNING : USE BY PREGNANT OR BREASTFEEDING WOMEN OR BY WOMEN PLANNING TO BECOME PREGNANT MAY RESULT IN FETAL INJURY, PRETERM BIRTH, LOW BIRTHWEIGHT OR DEVELOPMENTAL PROBLEMS FOR THE CHILD.
ACTIVATION TIME 20-60 MINUTES
THIRD PARTY LAB TESTED FOR POTENCY. THE ACTUAL VALUE OF CANNABINOIDS MAY VARY FROM THE REPORTED VALUE BY +/- 20%.

```html
<!DOCTYPE html>
<html lang="en">
<head>
<meta charset="utf-8">
<title>Gummy Oval Mylar Bag – Dieline</title>
<link rel="stylesheet" href="https://fonts.googleapis.com/css2?family=Bebas+Neue&family=Oswald:wght@300;500;700&family=Tinos&display=swap">
<style>
  :root {
    --bag-black: #050707;
    --dieline-green: #1f9a3e;
    --label-white: #ffffff;
    --brand-red: #c8313b;
    --warn-yellow: #f4e313;
    --badge-green: #1e7a3a;
    --leaf-green: #3aa142;
    --ink: #0a0a0a;
    --dim-grey: #3b3b3b;
  }
  html, body { margin: 0; padding: 0; }
  body {
    width: 1019px; height: 1200px; overflow: hidden;
    background: #ffffff;
  }
  .dieline-sheet { display: block; width: 1019px; height: 1200px; }
  .die-line { fill: none; stroke: var(--dieline-green); stroke-width: 2; }
  .die-dash { fill: none; stroke: var(--dieline-green); stroke-width: 2; stroke-dasharray: 12 9; }
  .dim-line { fill: none; stroke: var(--dieline-green); stroke-width: 3; }
  .dim-text { font-family: 'Tinos', serif; font-size: 19px; fill: var(--dim-grey); }
  .brand-name { font-family: 'Oswald', sans-serif; font-weight: 700; font-size: 96px; fill: var(--brand-red); letter-spacing: 2px; }
  .band-title { font-family: 'Bebas Neue', sans-serif; font-size: 50px; fill: var(--label-white); }
  .strength { font-family: 'Bebas Neue', sans-serif; font-size: 44px; fill: var(--ink); }
  .dose { font-family: 'Oswald', sans-serif; font-weight: 700; font-size: 76px; fill: var(--ink); }
  .dose-sub { font-family: 'Oswald', sans-serif; font-weight: 500; font-size: 17px; letter-spacing: 6px; fill: var(--ink); }
  .fine-print { font-family: 'Oswald', sans-serif; font-weight: 300; font-size: 10.5px; fill: var(--ink); }
  .serving { font-family: 'Bebas Neue', sans-serif; font-size: 27px; fill: var(--label-white); }
  .net-weight { font-family: 'Oswald', sans-serif; font-weight: 300; font-size: 11px; fill: var(--ink); }
  .warn-mark { font-family: 'Oswald', sans-serif; font-weight: 700; font-size: 30px; fill: var(--ink); }
  .back-copy { font-family: 'Oswald', sans-serif; font-weight: 300; font-size: 14.5px; fill: var(--label-white); }
  .back-copy .lead { font-weight: 700; }
  .pregnancy-copy { font-family: 'Oswald', sans-serif; font-weight: 300; font-size: 12.6px; fill: var(--ink); }
</style>
</head>
<body>
<svg class="dieline-sheet" viewBox="0 0 1760 2100" preserveAspectRatio="xMidYMid meet" xmlns="http://www.w3.org/2000/svg">
  <defs>
    <linearGradient id="leafTone" x1="0" y1="0" x2="0" y2="1">
      <stop offset="0" stop-color="#55b84a"/>
      <stop offset="1" stop-color="#1f7d35"/>
    </linearGradient>

    <!-- Half of the pouch structure: top panel + hang hole + zipper -->
    <g id="pouch-half">
      <rect class="die-line" x="10" y="10" width="510" height="761" rx="30"/>
      <circle class="die-line" cx="265" cy="44" r="15"/>
      <line class="die-line" x1="10" y1="122" x2="520" y2="122"/>
      <line class="die-line" x1="10" y1="131" x2="520" y2="131"/>
      <line class="die-dash" x1="10" y1="94" x2="520" y2="94"/>
      <line class="die-dash" x1="10" y1="160" x2="520" y2="160"/>
      <line class="die-dash" x1="35" y1="10" x2="35" y2="745"/>
      <line class="die-dash" x1="495" y1="10" x2="495" y2="745"/>
      <line class="die-dash" x1="35" y1="745" x2="495" y2="745"/>
      <path class="die-line" d="M10 66 L22 72 L10 78"/>
      <path class="die-line" d="M520 66 L508 72 L520 78"/>
    </g>

    <!-- Full pouch outline: outer black body, gusset, mirrored halves -->
    <g id="pouch">
      <rect x="0" y="0" width="530" height="1845" rx="42" fill="var(--bag-black)"/>
      <use href="#pouch-half"/>
      <use href="#pouch-half" transform="rotate(180 265 922.5)"/>
      <rect class="die-line" x="10" y="771" width="510" height="303" rx="30"/>
      <rect class="die-dash" x="35" y="796" width="460" height="252" rx="8"/>
    </g>

    <!-- Front label -->
    <g id="front-label">
      <rect x="66" y="192" width="397" height="508" rx="16" fill="var(--label-white)"/>
      <g role="img" aria-label="Cannabis leaf illustration">
        <ellipse cx="162" cy="242" rx="38" ry="34" fill="url(#leafTone)"/>
      </g>
      <text class="brand-name" x="265" y="352" text-anchor="middle">KORRO'S</text>
      <rect x="78" y="361" width="373" height="57" fill="var(--ink)"/>
      <text class="band-title" x="265" y="408" text-anchor="middle">BEST THC GUMMIES</text>

      <g class="warn-icon">
        <path d="M82 445 L133 445 L107.5 490 Z" fill="var(--warn-yellow)" stroke="var(--ink)" stroke-width="4" stroke-linejoin="round"/>
        <text class="warn-mark" x="107.5" y="477" text-anchor="middle" font-size="24">!</text>
      </g>
      <g class="warn-icon">
        <path d="M397 445 L448 445 L422.5 490 Z" fill="var(--warn-yellow)" stroke="var(--ink)" stroke-width="4" stroke-linejoin="round"/>
        <text class="warn-mark" x="422.5" y="477" text-anchor="middle" font-size="24">!</text>
      </g>
      <text class="strength" x="265" y="477" text-anchor="middle">TRIPLE STRENGTH</text>

      <path d="M84 498 L130 498 L107 542 Z" fill="var(--badge-green)"/>
      <text class="dose" x="277" y="545" text-anchor="middle">300 MG</text>
      <text class="dose-sub" x="268" y="569" text-anchor="middle">HIGH DOSE GUMMY OVALS</text>

      <text class="fine-print" x="265" y="599" text-anchor="middle" textLength="373" lengthAdjust="spacingAndGlyphs">THIS PRODUCT IS INTENDED FOR CAREGIVER TO PATIENT TRANSFER ONLY AND SHALL NOT BE SOLD.</text>
      <rect x="78" y="606" width="373" height="58" fill="var(--ink)"/>
      <text class="serving" x="265" y="633" text-anchor="middle">SERVING SIZE: 1 GUMMY = 15 MG THC</text>
      <text class="serving" x="265" y="658" text-anchor="middle">APPROX 20 THC GUMMIES PER PACK</text>
      <text class="net-weight" x="265" y="685" text-anchor="middle">NET WT. 96 G (packaged by weight*)</text>
    </g>

    <!-- Back label copy -->
    <g id="back-copy">
      <path d="M98 201 L164 201 L131 258 Z" fill="var(--label-white)"/>
      <path d="M106 206 L156 206 L131 250 Z" fill="var(--badge-green)"/>
      <text class="back-copy" x="83" y="293"><tspan class="lead">INGREDIENTS:</tspan> CORN SYRUP, WATER, SUGAR, GELATIN, ACTIVATED THC</text>
      <text class="back-copy" x="83" y="311">(FROM MICHIGAN GROWN CANNABIS), CITRIC ACID, VEGETABLE OIL,</text>
      <text class="back-copy" x="83" y="329">NATURAL AND ARTIFICIAL FLAVORS AND COLORS, CARNAUBA WAX</text>
      <text class="back-copy" x="83" y="365"><tspan class="lead">WARNING:</tspan> CONTAINS THC.</text>
      <text class="back-copy" x="83" y="401">KEEP OUT OF REACH OF CHILDREN</text>
      <text class="back-copy" x="83" y="419">CORVANE TOXIN HELP BUREAU 1 800 555 0147</text>
      <text class="back-copy" x="83" y="455">MADE IN COMPLIANCE WITH THE 2008 MEDICAL MARIJUANA ACT</text>
      <text class="back-copy" x="83" y="491">FOR USE BY INDIVIDUALS 21 YEARS OF AGE OR OLDER OR BY REGISTERED</text>
      <text class="back-copy" x="83" y="509">QUALIFYING PATIENTS ONLY.</text>
      <rect x="83" y="526" width="360" height="62" rx="3" fill="var(--label-white)"/>
      <text class="pregnancy-copy" x="96" y="545">WARNING : USE BY PREGNANT OR BREASTFEEDING WOMEN OR BY WOMEN</text>
      <text class="pregnancy-copy" x="96" y="561">PLANNING TO BECOME PREGNANT MAY RESULT IN FETAL INJURY, PRETERM</text>
      <text class="pregnancy-copy" x="96" y="577">BIRTH, LOW BIRTHWEIGHT OR DEVELOPMENTAL PROBLEMS FOR THE CHILD.</text>
      <text class="back-copy" x="83" y="617">ACTIVATION TIME 20-60 MINUTES</text>
      <text class="back-copy" x="83" y="653">THIRD PARTY LAB TESTED FOR POTENCY. THE ACTUAL VALUE OF</text>
      <text class="back-copy" x="83" y="671">CANNABINOIDS MAY VARY FROM THE REPORTED VALUE BY +/- 20%.</text>
    </g>
  </defs>

  <!-- Left pouch: front on top, back rotated on bottom -->
  <g class="pouch-left" transform="translate(305 117)">
    <use href="#pouch"/>
    <use href="#front-label"/>
    <use href="#back-copy" transform="rotate(180 265 922.5)"/>
    <line class="die-line" x1="265" y1="-10" x2="265" y2="29"/>
  </g>

  <!-- Right pouch: back on top, front rotated on bottom -->
  <g class="pouch-right" transform="translate(930 117)">
    <use href="#pouch"/>
    <use href="#back-copy"/>
    <use href="#front-label" transform="rotate(180 265 922.5)"/>
    <line class="die-line" x1="265" y1="1816" x2="265" y2="1860"/>
  </g>

  <!-- Dimensions -->
  <g class="dimensions">
    <path class="dim-line" d="M245 125 H265 M255 125 V275 M245 275 H265"/>
    <path class="dim-line" d="M280 125 H300 M290 125 V188 M280 188 H300"/>
    <path class="dim-line" d="M280 212 H300 M290 212 V275 M280 275 H300"/>
    <text class="dim-text" transform="translate(236 200) rotate(90)" text-anchor="middle">30mm</text>
    <text class="dim-text" transform="translate(271 157) rotate(90)" text-anchor="middle">13mm</text>
    <text class="dim-text" transform="translate(271 244) rotate(90)" text-anchor="middle">13mm</text>
    <text class="dim-text" transform="translate(561 78) rotate(90)" text-anchor="middle">102mm</text>
    <text class="dim-text" transform="translate(849 512) rotate(90)" text-anchor="middle">152mm</text>
    <text class="dim-text" transform="translate(849 1035) rotate(90)" text-anchor="middle">60mm</text>
    <text class="dim-text" transform="translate(849 1560) rotate(90)" text-anchor="middle">152mm</text>
    <text class="dim-text" transform="translate(915 512) rotate(-90)" text-anchor="middle">152mm</text>
    <text class="dim-text" transform="translate(915 1045) rotate(-90)" text-anchor="middle">60mm</text>
    <text class="dim-text" transform="translate(915 1562) rotate(-90)" text-anchor="middle">152mm</text>
    <path class="dim-line" d="M1495 1802 H1515 M1505 1802 V1952 M1495 1952 H1515"/>
    <path class="dim-line" d="M1460 1802 H1480 M1470 1802 V1866 M1460 1866 H1480"/>
    <path class="dim-line" d="M1460 1888 H1480 M1470 1888 V1952 M1460 1952 H1480"/>
    <text class="dim-text" transform="translate(1527 1877) rotate(-90)" text-anchor="middle">30mm</text>
    <text class="dim-text" transform="translate(1492 1834) rotate(-90)" text-anchor="middle">13mm</text>
    <text class="dim-text" transform="translate(1492 1920) rotate(-90)" text-anchor="middle">13mm</text>
    <text class="dim-text" transform="translate(1202 2000) rotate(-90)" text-anchor="middle">102mm</text>
  </g>
</svg>
</body>
</html>
```